Valtrix Inc

Hello.

I would like to take a wordpress ecomm template and turn it into a website that can display 100s of domain listings with short text box for description and a price .
One link to quibblepay.example for immediate payment and with the confirmation/decline letter/email .
Five - six pages, Home, about us, domains, contact us, . Several columns or scrolling page for the domain page. I want to list several hundred virtual domains for sale .
Like a portfolio website but lists domain text .
This will be hosted on my server. On my domain.

Target Market(s)

End users, business owners, store front managers, online entpenauers , ect

Industry/Entity Type

Information Technology

Number of Pages Required

5+ page

Font styles to use
Sans Serif

Colors
0455a3
f78f20
abd036

Requirements
Must have
• Lots of white space, clean professional look . fast loading , use of greens and blues. Easy to read font.
• big headers , several - three different headers that rotate or move or clicks.
• A few current stock photos.
Should not have
• slow loading photos.
• More than two photos on any one page.

```html
<!DOCTYPE html>
<html lang="en">
<head>
<meta charset="utf-8">
<title>Valtrix Inc — Domains for Sale</title>
<link href="https://fonts.googleapis.com/css2?family=Open+Sans:wght@400;600;700;800&family=Montserrat:wght@700;800&display=swap" rel="stylesheet">
<style>
:root{
  --blue:#0455a3;
  --blue-deep:#033f7a;
  --orange:#f78f20;
  --green:#abd036;
  --dark:#1f2226;
  --darker:#16181b;
  --ink:#333;
  --muted:#8a8f96;
  --line:#d9dde2;
  --row-alt:#f4f6f8;
  --white:#fff;
}
*{box-sizing:border-box;margin:0;padding:0}
html,body{width:1200px;height:2228px;overflow:hidden;background:var(--white);font-family:"Open Sans",Arial,sans-serif;color:var(--ink)}
.page{position:relative;width:1200px;height:2228px}

/* hero */
.hero{position:absolute;left:0;top:0;width:1200px;height:500px}
.hero-photo{position:absolute;inset:0;background:linear-gradient(115deg,#2a3a4c 0%,#4a6680 40%,#7d93a8 62%,#3b4f64 100%)}
.hero-shade{position:absolute;inset:0;background:linear-gradient(180deg,rgba(10,18,28,.75) 0%,rgba(10,18,28,.25) 30%,rgba(10,18,28,.2) 70%,rgba(10,18,28,.55) 100%)}
.topbar{position:absolute;right:0;top:0;width:540px;height:34px;background:var(--green);display:flex;align-items:center;justify-content:flex-end;gap:30px;padding-right:56px;font-size:13px;font-weight:600;color:var(--white);clip-path:polygon(24px 0,100% 0,100% 100%,0 100%)}
.topbar span{display:flex;align-items:center;gap:8px}
.brand{position:absolute;left:72px;top:58px;display:flex;align-items:center;gap:12px;font-family:"Montserrat",sans-serif;font-weight:800;font-size:46px;letter-spacing:1px;color:var(--white)}
.brand .dot{width:16px;height:16px;border-radius:50%;background:var(--green)}
.nav{position:absolute;right:72px;top:92px;display:flex;align-items:center;gap:28px;font-size:15px;font-weight:700;color:var(--white)}
.nav a{color:inherit;text-decoration:none;padding-bottom:6px}
.nav a.active{color:var(--green);border-bottom:3px solid var(--green)}
.nav .search-btn{background:var(--blue);padding:10px 16px;border-bottom:none}
.search{position:absolute;left:180px;top:360px;width:700px;height:58px;display:flex}
.search-field{flex:1;background:rgba(255,255,255,.35);border:2px solid rgba(255,255,255,.55);display:flex;align-items:center;gap:14px;padding:0 18px;font-size:26px;font-weight:700;color:#2b3440}
.search-go{width:120px;background:#243140;color:var(--white);font-weight:700;font-size:16px;display:flex;align-items:center;justify-content:center}

/* promo band */
.promo{position:absolute;left:0;top:500px;width:1200px;height:160px;background:var(--blue);text-align:center;color:var(--white);padding-top:42px}
.promo p{font-size:25px;font-weight:700}
.promo h2{font-family:"Montserrat",sans-serif;font-weight:800;font-size:44px;margin-top:8px;letter-spacing:.5px}
.promo h2 em{font-style:normal;color:var(--green)}

/* listing */
.listing-title{position:absolute;left:0;top:710px;width:1200px;text-align:center;font-size:30px;font-weight:600;letter-spacing:1px;color:var(--orange)}
.listing-title b{color:var(--green);font-weight:600}
.domains{position:absolute;left:72px;top:780px;width:1056px;border-collapse:collapse;font-size:12.5px;border:1px solid var(--line)}
.domains th{height:38px;background:#eef1f4;color:var(--blue);font-size:14px;font-weight:700;text-align:left;padding:0 12px;border:1px solid var(--line)}
.domains th .hd{display:flex;align-items:center;gap:10px}
.domains th.pay{color:var(--blue-deep);font-size:18px;font-weight:800}
.domains td{height:26px;padding:0 12px;border-right:1px solid var(--line);border-bottom:1px solid #e8ebee}
.domains tr:nth-child(even) td{background:var(--row-alt)}
.domains td.price{color:#555}
.domains td.pay{text-align:center}
.pay-mark{display:inline-block;width:11px;height:13px;background:var(--blue);border-radius:2px;vertical-align:middle}
.col-name{width:230px}.col-desc{width:550px}.col-price{width:96px}

/* footer */
.footer{position:absolute;left:0;top:1940px;width:1200px;height:252px;background:var(--dark);color:#c8ccd1}
.footer .brand{left:72px;top:100px;font-size:42px}
.about{position:absolute;left:500px;top:40px;width:290px}
.footer h4{font-size:15px;font-weight:700;color:var(--white);margin-bottom:14px;letter-spacing:.5px}
.about p{font-size:11.5px;line-height:1.55}
.contact{position:absolute;left:858px;top:40px;width:270px}
.field{height:22px;background:var(--white);margin-bottom:8px;font-size:10px;color:var(--muted);padding:4px 8px}
.field.msg{height:54px}
.submit{display:inline-block;background:var(--darker);color:var(--white);font-size:11px;font-weight:700;padding:6px 16px;border:1px solid #444}
.legal{position:absolute;left:0;top:2192px;width:1200px;height:36px;background:var(--blue);display:flex;align-items:center;justify-content:space-between;padding:0 72px;color:var(--white);font-size:11px;font-weight:600}
.socials{display:flex;gap:8px}
.socials i{display:block;width:18px;height:18px;border-radius:50%;background:var(--white)}
</style>
</head>
<body>
<div class="page">

  <header class="hero">
    <div class="hero-photo" role="img" aria-label="Close-up photo of a browser address bar showing https://www"></div>
    <div class="hero-shade"></div>
    <div class="topbar">
      <span><svg width="13" height="13" viewBox="0 0 24 24"><path fill="#fff" d="M6.6 10.8a15.1 15.1 0 006.6 6.6l2.2-2.2c.3-.3.7-.4 1-.2 1.1.4 2.3.6 3.6.6.6 0 1 .4 1 1V20c0 .6-.4 1-1 1C10.6 21 3 13.4 3 4c0-.6.4-1 1-1h3.5c.6 0 1 .4 1 1 0 1.2.2 2.4.6 3.6.1.3 0 .7-.2 1z"/></svg>1-800-555-0199</span>
      <span><svg width="14" height="11" viewBox="0 0 24 18"><rect x="1" y="1" width="22" height="16" rx="2" fill="none" stroke="#fff" stroke-width="2"/><path d="M1 2l11 8 11-8" fill="none" stroke="#fff" stroke-width="2"/></svg>info@valtrix.example</span>
    </div>
    <div class="brand">VALTRIX<span class="dot"></span></div>
    <nav class="nav">
      <a class="active" href="#">HOME</a>
      <a href="#">ABOUT US</a>
      <a href="#">DOMAINS</a>
      <a href="#">CONTACT</a>
      <a class="search-btn" href="#">SEARCH DOMAIN</a>
    </nav>
    <div class="search">
      <div class="search-field">
        <svg width="24" height="24" viewBox="0 0 24 24"><circle cx="10" cy="10" r="7" fill="none" stroke="#2b3440" stroke-width="3"/><path d="M15 15l7 7" stroke="#2b3440" stroke-width="3"/></svg>
        www.
      </div>
      <div class="search-go">SEARCH</div>
    </div>
  </header>

  <section class="promo">
    <p>Are you looking for virtual domains for sale? Or simply need a new domain?</p>
    <h2>YOU HAVE COME TO <em>THE RIGHT PLACE.</em></h2>
  </section>

  <h3 class="listing-title"><b>DOMAINS</b> FOR SALE</h3>

  <table class="domains">
    <thead>
      <tr>
        <th class="col-name"><span class="hd"><svg width="14" height="14" viewBox="0 0 14 14"><circle cx="7" cy="7" r="6" fill="none" stroke="#0455a3" stroke-width="2"/></svg>DOMAIN NAME</span></th>
        <th class="col-desc"><span class="hd"><svg width="14" height="14" viewBox="0 0 14 14"><path d="M2 3h10M2 7h10M2 11h7" stroke="#0455a3" stroke-width="2"/></svg>DESCRIPTIONS</span></th>
        <th class="col-price"><span class="hd"><svg width="14" height="14" viewBox="0 0 14 14"><rect x="1" y="1" width="12" height="12" fill="none" stroke="#0455a3" stroke-width="2"/></svg>PRICE</span></th>
        <th class="pay">QuibblePay</th>
      </tr>
    </thead>
    <tbody>
      <tr><td>abx.com</td><td>Lorem ipsum dolor sit amet, consectetur adipiscing elit.</td><td class="price">$2.00</td><td class="pay"><span class="pay-mark"></span></td></tr>
      <tr><td>zbea.com</td><td>Ut wisi enim ad minim veniam, quis nostrud.</td><td class="price">$3.00</td><td class="pay"><span class="pay-mark"></span></td></tr>
      <tr><td>abcecop.com</td><td>Nam liber tempor cum soluta nobis eleifend option.</td><td class="price">$2.00</td><td class="pay"><span class="pay-mark"></span></td></tr>
      <tr><td>abccompany.com</td><td>Typi non habent claritatem insitam, est usus legentis.</td><td class="price">$5.00</td><td class="pay"><span class="pay-mark"></span></td></tr>
      <tr><td>auspol.com</td><td>Claritas est etiam processus dynamicus, qui sequitur mutationem.</td><td class="price">$2.00</td><td class="pay"><span class="pay-mark"></span></td></tr>
      <tr><td>avquile.com</td><td>Lorem ipsum dolor sit amet, consectetur adipiscing elit.</td><td class="price">$3.00</td><td class="pay"><span class="pay-mark"></span></td></tr>
      <tr><td>acquire.com</td><td>Ut wisi enim ad minim veniam, quis nostrud.</td><td class="price">$2.00</td><td class="pay"><span class="pay-mark"></span></td></tr>
      <tr><td>actnmarledge.com</td><td>Nam liber tempor cum soluta nobis eleifend option.</td><td class="price">$7.00</td><td class="pay"><span class="pay-mark"></span></td></tr>
      <tr><td>act.none</td><td>Typi non habent claritatem insitam, est usus legentis.</td><td class="price">$2.00</td><td class="pay"><span class="pay-mark"></span></td></tr>
      <tr><td>actovy.com</td><td>Claritas est etiam processus dynamicus, qui sequitur mutationem.</td><td class="price">$3.00</td><td class="pay"><span class="pay-mark"></span></td></tr>
      <tr><td>actorpration.com</td><td>Lorem ipsum dolor sit amet, consectetur adipiscing elit.</td><td class="price">$2.00</td><td class="pay"><span class="pay-mark"></span></td></tr>
      <tr><td>actingcorp.com</td><td>Ut wisi enim ad minim veniam, quis nostrud.</td><td class="price">$4.00</td><td class="pay"><span class="pay-mark"></span></td></tr>
      <tr><td>admisions.com</td><td>Nam liber tempor cum soluta nobis eleifend option.</td><td class="price">$2.00</td><td class="pay"><span class="pay-mark"></span></td></tr>
      <tr><td>aviscart.com</td><td>Typi non habent claritatem insitam, est usus legentis.</td><td class="price">$3.00</td><td class="pay"><span class="pay-mark"></span></td></tr>
      <tr><td>aulecant.com</td><td>Claritas est etiam processus dynamicus, qui sequitur mutationem.</td><td class="price">$2.00</td><td class="pay"><span class="pay-mark"></span></td></tr>
      <tr><td>autobuilders.com</td><td>Lorem ipsum dolor sit amet, consectetur adipiscing elit.</td><td class="price">$6.00</td><td class="pay"><span class="pay-mark"></span></td></tr>
      <tr><td>autodetails.com</td><td>Ut wisi enim ad minim veniam, quis nostrud.</td><td class="price">$2.00</td><td class="pay"><span class="pay-mark"></span></td></tr>
      <tr><td>automeyarls.com</td><td>Nam liber tempor cum soluta nobis eleifend option.</td><td class="price">$3.00</td><td class="pay"><span class="pay-mark"></span></td></tr>
      <tr><td>autony.com</td><td>Typi non habent claritatem insitam, est usus legentis.</td><td class="price">$7.00</td><td class="pay"><span class="pay-mark"></span></td></tr>
      <tr><td>avlerj.com</td><td>Claritas est etiam processus dynamicus, qui sequitur mutationem.</td><td class="price">$2.00</td><td class="pay"><span class="pay-mark"></span></td></tr>
      <tr><td>avionline.com</td><td>Lorem ipsum dolor sit amet, consectetur adipiscing elit.</td><td class="price">$3.00</td><td class="pay"><span class="pay-mark"></span></td></tr>
      <tr><td>bern.com</td><td>Ut wisi enim ad minim veniam, quis nostrud.</td><td class="price">$2.00</td><td class="pay"><span class="pay-mark"></span></td></tr>
      <tr><td>bosgoods.com</td><td>Nam liber tempor cum soluta nobis eleifend option.</td><td class="price">$2.00</td><td class="pay"><span class="pay-mark"></span></td></tr>
      <tr><td>bridesandgroomsnetwork.com</td><td>Typi non habent claritatem insitam, est usus legentis.</td><td class="price">$3.00</td><td class="pay"><span class="pay-mark"></span></td></tr>
      <tr><td>bridecrowd.com</td><td>Claritas est etiam processus dynamicus, qui sequitur mutationem.</td><td class="price">$2.00</td><td class="pay"><span class="pay-mark"></span></td></tr>
      <tr><td>benmaute.com</td><td>Lorem ipsum dolor sit amet, consectetur adipiscing elit.</td><td class="price">$4.00</td><td class="pay"><span class="pay-mark"></span></td></tr>
      <tr><td>canbolars.com</td><td>Ut wisi enim ad minim veniam, quis nostrud.</td><td class="price">$2.00</td><td class="pay"><span class="pay-mark"></span></td></tr>
      <tr><td>carbluster.com</td><td>Nam liber tempor cum soluta nobis eleifend option.</td><td class="price">$3.00</td><td class="pay"><span class="pay-mark"></span></td></tr>
      <tr><td>carfronds.com</td><td>Typi non habent claritatem insitam, est usus legentis.</td><td class="price">$2.00</td><td class="pay"><span class="pay-mark"></span></td></tr>
      <tr><td>carforcad.com</td><td>Claritas est etiam processus dynamicus, qui sequitur mutationem.</td><td class="price">$5.00</td><td class="pay"><span class="pay-mark"></span></td></tr>
      <tr><td>circlecenter.com</td><td>Lorem ipsum dolor sit amet, consectetur adipiscing elit.</td><td class="price">$2.00</td><td class="pay"><span class="pay-mark"></span></td></tr>
      <tr><td>circledash.com</td><td>Ut wisi enim ad minim veniam, quis nostrud.</td><td class="price">$3.00</td><td class="pay"><span class="pay-mark"></span></td></tr>
      <tr><td>circlerestaurant.com</td><td>Nam liber tempor cum soluta nobis eleifend option.</td><td class="price">$2.00</td><td class="pay"><span class="pay-mark"></span></td></tr>
      <tr><td>cornlink.com</td><td>Typi non habent claritatem insitam, est usus legentis.</td><td class="price">$2.00</td><td class="pay"><span class="pay-mark"></span></td></tr>
      <tr><td>corecorporation.com</td><td>Claritas est etiam processus dynamicus, qui sequitur mutationem.</td><td class="price">$3.00</td><td class="pay"><span class="pay-mark"></span></td></tr>
      <tr><td>coveline.com</td><td>Lorem ipsum dolor sit amet, consectetur adipiscing elit.</td><td class="price">$2.00</td><td class="pay"><span class="pay-mark"></span></td></tr>
      <tr><td>crestmarket.com</td><td>Ut wisi enim ad minim veniam, quis nostrud.</td><td class="price">$4.00</td><td class="pay"><span class="pay-mark"></span></td></tr>
      <tr><td>cubeport.com</td><td>Nam liber tempor cum soluta nobis eleifend option.</td><td class="price">$2.00</td><td class="pay"><span class="pay-mark"></span></td></tr>
      <tr><td>curveway.com</td><td>Typi non habent claritatem insitam, est usus legentis.</td><td class="price">$3.00</td><td class="pay"><span class="pay-mark"></span></td></tr>
      <tr><td>cyberlane.com</td><td>Claritas est etiam processus dynamicus, qui sequitur mutationem.</td><td class="price">$2.00</td><td class="pay"><span class="pay-mark"></span></td></tr>
    </tbody>
  </table>

  <footer class="footer">
    <div class="brand">VALTRIX<span class="dot"></span></div>
    <div class="about">
      <h4>ABOUT VALTRIX, INC</h4>
      <p>Lorem ipsum dolor sit amet, consectetur adipiscing elit, sed diam nonummy nibh euismod tincidunt ut laoreet dolore magna aliquam erat volutpat. Ut wisi enim ad minim veniam, quis nostrud exerci tation ullamcorper suscipit lobortis nisl ut aliquip ex ea commodo consequat.</p>
    </div>
    <div class="contact">
      <h4>CONTACT US</h4>
      <div class="field">Name</div>
      <div class="field">Email</div>
      <div class="field msg">Message</div>
      <span class="submit">SUBMIT</span>
    </div>
  </footer>
  <div class="legal">
    <span>COPYRIGHT © 2016 VALTRIX, INC. ALL RIGHTS RESERVED.</span>
    <span class="socials"><i></i><i></i><i></i></span>
  </div>

</div>
</body>
</html>
```